Create a packaging design and label for fruit company

I am after a packaging design and label (using the attached logo) for the following fruit combinations:

- rockmelon
- watermelon
- pineapple
- fruit salad

I am after a design for these options - label and unique design package. I'd like to see these options on there own as well as mocked up on the packaging. The design needs to be cohesive but distinctive in some way for each fruit combination.

```html
<!DOCTYPE html>
<html lang="en">
<head>
<meta charset="UTF-8">
<title>Fruit Salad Pack Label</title>
<link href="https://fonts.googleapis.com/css2?family=Arimo:wght@500&family=Righteous&display=swap" rel="stylesheet">
<style>
  :root {
    --backdrop: #cdb594;
    --wood-dark: #6e3a22;
    --wood-mid: #9a5434;
    --wood-light: #b46a45;
    --title-yellow: #f5c518;
    --name-amber: #f0b33c;
    --logo-white: #f4efe9;
    --fruit-yellow: #f4c52a;
    --fruit-red: #e5484a;
    --fruit-orange: #f09a3c;
  }
  html, body {
    margin: 0;
    padding: 0;
    width: 1200px;
    height: 807px;
    overflow: hidden;
    background: var(--backdrop);
  }
  .pack-label {
    position: absolute;
    left: 150px;
    top: 110px;
    width: 900px;
    height: 580px;
    overflow: hidden;
  }
  .wood-surface {
    position: absolute;
    inset: 0;
    background:
      linear-gradient(180deg, rgba(0,0,0,0.12) 0%, rgba(255,255,255,0.05) 45%, rgba(0,0,0,0.18) 100%),
      linear-gradient(90deg, var(--wood-dark) 0%, var(--wood-mid) 30%, var(--wood-light) 55%, var(--wood-mid) 80%, var(--wood-dark) 100%);
  }
  .brand {
    position: absolute;
    left: 40px;
    top: 70px;
    width: 190px;
    text-align: center;
    font-family: "Arimo", sans-serif;
    font-weight: 500;
    color: var(--logo-white);
  }
  .brand-mark {
    width: 34px;
    height: 34px;
    border-radius: 50%;
    background: var(--logo-white);
    margin: 0 auto 12px;
  }
  .brand-name {
    font-size: 22px;
    letter-spacing: 3px;
    line-height: 1.25;
  }
  .product-title {
    position: absolute;
    left: 317px;
    top: 96px;
    margin: 0;
    font-family: "Righteous", sans-serif;
    font-weight: 400;
    font-size: 62px;
    letter-spacing: 3px;
    color: var(--title-yellow);
    white-space: nowrap;
  }
  .fruit-list {
    position: absolute;
    left: 31px;
    top: 285px;
    margin: 0;
    padding: 0;
    list-style: none;
    font-family: "Arimo", sans-serif;
    font-weight: 500;
    font-size: 32px;
    line-height: 64px;
    color: var(--name-amber);
  }
  .fruit-photo {
    position: absolute;
    left: 344px;
    top: 223px;
    width: 420px;
    height: 285px;
    border-radius: 46% 46% 40% 40%;
    background:
      radial-gradient(circle at 22% 70%, var(--fruit-yellow) 0%, transparent 38%),
      radial-gradient(circle at 52% 78%, var(--fruit-red) 0%, transparent 40%),
      radial-gradient(circle at 82% 66%, var(--fruit-orange) 0%, transparent 38%),
      radial-gradient(ellipse at 55% 28%, #f2a862 0%, #d9835a 45%, transparent 75%);
  }
  .net-weight {
    position: absolute;
    right: 20px;
    bottom: 22px;
    font-family: "Righteous", sans-serif;
    font-size: 36px;
    color: var(--title-yellow);
  }
</style>
</head>
<body>
  <main class="pack-label">
    <div class="wood-surface" role="img" aria-label="Rustic wooden plank background"></div>

    <div class="brand">
      <div class="brand-mark"></div>
      <div class="brand-name">THE ORCHARD CROWN</div>
    </div>

    <h1 class="product-title">FRUIT SALAD</h1>

    <ul class="fruit-list">
      <li>Pineapple</li>
      <li>Watermelon</li>
      <li>Rockmelon</li>
    </ul>

    <div class="fruit-photo" role="img" aria-label="Bowl of diced melon and pineapple with slices of pineapple, watermelon and rockmelon"></div>

    <div class="net-weight">0,3 Kg</div>
  </main>
</body>
</html>
```